Opening soon Tufty Marvel Grooming Specialist

I need a flyer to be posted through peoples letter boxes for the opening of my dog grooming salon. It needs to be bright, bold and eye catching. Something cool and modern but not overly masculine or too feminine. Text to include salon phone number 07700900318, 50% discouunt for 1st 2 weeks of opening, owned and operated by ex-military dog handler and trainer and hollin and weavers level 3 professional dog groomer.

Salon

```html
<!DOCTYPE html>
<html lang="en">
<head>
<meta charset="utf-8">
<title>Tufty Marvel Grooming Specialist – Opening Flyer</title>
<link rel="stylesheet" href="https://fonts.googleapis.com/css2?family=Arimo:wght@400;700&display=swap">
<style>
  :root {
    --red: #d0142c;
    --red-deep: #8c0a1b;
    --white: #ffffff;
    --ink: #1d1d1d;
    --concrete-light: #b9b7b2;
    --concrete-dark: #77746f;
    --fur-light: #f1dcae;
    --fur-mid: #d9b77a;
    --shadow: rgba(0, 0, 0, 0.55);
  }
  * { box-sizing: border-box; margin: 0; padding: 0; }
  html, body { width: 855px; height: 1200px; overflow: hidden; background: #ffffff; }
  .flyer {
    position: relative;
    width: 855px;
    height: 1200px;
    overflow: hidden;
    font-family: "Arimo", Arial, sans-serif;
    color: var(--white);
  }
  .hero-photo {
    position: absolute;
    inset: 0;
    background:
      radial-gradient(ellipse 420px 560px at 640px 560px, var(--fur-light) 0%, var(--fur-mid) 55%, rgba(217,183,122,0) 78%),
      linear-gradient(160deg, var(--concrete-light) 0%, #a19e98 45%, var(--concrete-dark) 100%);
  }
  .bands { position: absolute; inset: 0; width: 855px; height: 1200px; }
  .phone {
    position: absolute;
    top: 30px;
    right: 40px;
    display: flex;
    align-items: center;
    gap: 12px;
    font-weight: 700;
    font-size: 46px;
    letter-spacing: 0.5px;
  }
  .phone svg { width: 34px; height: 42px; }
  .brand {
    position: absolute;
    top: 150px;
    left: 60px;
    width: 340px;
    display: flex;
    align-items: flex-start;
    gap: 16px;
    color: var(--ink);
  }
  .brand-dot {
    flex: none;
    width: 34px;
    height: 34px;
    margin-top: 10px;
    border-radius: 50%;
    background: var(--red);
  }
  .brand-name {
    font-weight: 700;
    font-size: 46px;
    line-height: 1.05;
    color: var(--ink);
  }
  .offer {
    position: absolute;
    left: 45px;
    top: 602px;
    width: 292px;
    height: 282px;
    border-radius: 24px;
    background: linear-gradient(180deg, var(--red) 0%, var(--red-deep) 100%);
    box-shadow: 0 0 0 3px rgba(255,255,255,0.85), 0 0 18px 6px rgba(255,255,255,0.7);
    text-align: center;
    font-weight: 700;
    line-height: 1;
    padding-top: 20px;
  }
  .offer-figure { font-size: 104px; letter-spacing: -2px; }
  .offer-terms { font-size: 33px; line-height: 1.05; margin-top: 6px; }
  .offer-word { font-size: 62px; margin-top: 2px; }
  .opening-date {
    position: absolute;
    left: 36px;
    top: 908px;
    font-weight: 700;
    font-size: 50px;
    line-height: 1.12;
    text-shadow: 2px 2px 3px var(--shadow), 0 0 8px var(--shadow);
  }
  .opening-date span { display: block; padding-left: 42px; }
  .credentials {
    position: absolute;
    left: 0;
    right: 0;
    top: 1062px;
    text-align: center;
    font-weight: 700;
    font-size: 24px;
    line-height: 1.45;
  }
  .address { display: inline-flex; align-items: center; gap: 8px; }
  .address svg { width: 20px; height: 20px; }
</style>
</head>
<body>
<main class="flyer">
  <div class="hero-photo" role="img" aria-label="Photograph of a smiling yellow Labrador with its tongue out, against a grey concrete wall"></div>

  <svg class="bands" viewBox="0 0 855 1200" aria-hidden="true">
    <defs>
      <linearGradient id="band-red" x1="0" y1="0" x2="0" y2="1">
        <stop offset="0" stop-color="#d0142c"/>
        <stop offset="1" stop-color="#9a0c1f"/>
      </linearGradient>
    </defs>
    <path d="M0 0 H855 V100 Q560 132 330 112 Q140 96 0 70 Z" fill="url(#band-red)"/>
    <path d="M0 1032 Q420 1000 855 1010 V1200 H0 Z" fill="url(#band-red)"/>
  </svg>

  <div class="phone">
    <svg viewBox="0 0 24 30" aria-hidden="true">
      <path d="M6 1 C3 2 1 5 2 10 C4 18 8 25 14 28 C17 29.5 19 28.5 20.5 26 L17 20.5 C16 19.5 14.5 20.5 13.5 21 C11.5 18.5 9.5 14 9 10.5 C10 10 11.6 9.4 11.5 8 L10 1.5 C9 0.6 7.5 0.6 6 1 Z" fill="#ffffff"/>
    </svg>
    <span>07700900318</span>
  </div>

  <div class="brand">
    <span class="brand-dot" aria-hidden="true"></span>
    <span class="brand-name">Tufty Marvel Grooming Specialist</span>
  </div>

  <section class="offer">
    <div class="offer-figure">50%</div>
    <div class="offer-terms">discount for<br>1st 2 weeks of</div>
    <div class="offer-word">opening</div>
  </section>

  <p class="opening-date">Opening on:<span>25/08/2014</span></p>

  <footer class="credentials">
    <p>Owned by Ex-Military Dog Handler and Trainer.</p>
    <p>Qualified Hollin and Weavers Level 3 Dog Groomer</p>
    <p class="address">
      <svg viewBox="0 0 20 20" aria-hidden="true"><path d="M10 2 L19 10 H16 V18 H12 V13 H8 V18 H4 V10 H1 Z" fill="#ffffff"/></svg>
      Unit 3, Alder Park, Mill Road, Brackenford, Cheshire
    </p>
  </footer>
</main>
</body>
</html>
```